Have you played "zo"?

I am creating a card game called “ZO” and will need help designing the following:

The name of the game is “zo”. So I need a logo and I want zo to be the word “zo” but obviously I want to word zo to have its own style and look. So zo will be recognizable. The “zo” logo will be on the back of all the cards and on the box that I sell zo in.

There will be cards numbered 1-10 in the game and I want zo to be a basic design with some color on each of those cards. Preferably where the number is listed in 2 of the 4 corners in smaller text so that you can always see what card zo is, whether zo is upside down or not. I visualize the number being large in the center of the card as well. I want there to be some sort of simple and modern design element to the card that we can repeat on all the numbered cards. All the numbered cards being the same color is fine, but I am also ok with having some variation of the color if you like that.

There are 4 action cards in the deck that will have there own art work on card. I want the same theme to carry between all the actions cards and that action is that whatever the descriptive word is that its happening to the word “zo”. zo will make more sense when you see the categories below. Each action card will have a short sentence on the bottom describing how house the card so design the card knowing that.
“BURN zo” card-The word “zo” either being burned in a fire or the word “zo” looking burned standing alone or maybe the word “zo” is on fire or its seared. If you have other ideas I am excited to see them.
“Add zo” card- (addition) This card allows you to add other card values together. So something that show addiction happening or even the word “zo: being added. i.e. i+t=zo
“Reset zo”- I like the idea of this one having a reset button on zo and the word “zo” is built in to the reset button. The I and the t being curved to look like a reset button if that makes sense.
“Take zo”- This card forces you to take the entire discard pile so its not a BAD card. Do whatever you come up with here. I want the card to be darker in color since its a BAD card. Something that shows “zo” being taken.

I want everything to be very simple and clean looking. I want to design and feel of the cards to be modern. I really like logos like Vorda and Quimby. Very basic but strong. I included some basic logos I found online just to give an example of simple. Simple with a pop. Something that still draws attention and maybe the color helps with that.

Target Market(s)

Families and college age gamers

Font styles to use
Sans Serif

Colors

Designer to choose colors to be used in the design.

Requirements
Must have
• A simple feel to the design with some color
Nice to have
• a playful feel to the design
Should not have
• complex designs or art work

```html
<!DOCTYPE html>
<html lang="en">
<head>
<meta charset="utf-8">
<title>ZO — Card Set</title>
<link href="https://fonts.googleapis.com/css2?family=Rubik+Mono+One&family=Fira+Sans+Extra+Condensed:wght@600&display=swap" rel="stylesheet">
<style>
  :root {
    --page: #ffffff;
    --card-face: #e6e6e6;
    --card-edge: #c9c9c9;
    --red: #ef4c3c;
    --red-dark: #9b1c1f;
    --green: #35b589;
    --green-dark: #1d5e44;
    --purple: #9b2f9e;
    --purple-dark: #5b1a5c;
    --blue: #1e94c4;
    --blue-dark: #2b6e9c;
    --ink: #111111;
  }
  html, body {
    margin: 0;
    padding: 0;
    width: 900px;
    height: 1200px;
    overflow: hidden;
    background: var(--page);
  }
  .deck {
    position: relative;
    width: 900px;
    height: 1200px;
  }
  .card {
    position: absolute;
    width: 129px;
    height: 207px;
    background: var(--card-face);
    border: 1px solid var(--card-edge);
    box-shadow: 0 1px 3px rgba(0,0,0,0.35);
    box-sizing: border-box;
    overflow: hidden;
  }
  .col-1 { left: 94px; }
  .col-2 { left: 289px; }
  .col-3 { left: 482px; }
  .col-4 { left: 676px; }
  .row-1 { top: 96px; }
  .row-2 { top: 362px; }
  .row-3 { top: 630px; }
  .row-4 { top: 896px; }

  .number-card .value,
  .number-card .corner {
    font-family: "Rubik Mono One", sans-serif;
    position: absolute;
    line-height: 1;
  }
  .number-card .value {
    left: 0; right: 0;
    top: 50%;
    transform: translateY(-50%);
    text-align: center;
    font-size: 88px;
    letter-spacing: -4px;
  }
  .number-card .value.two-digit { font-size: 64px; letter-spacing: -6px; }
  .number-card .corner { font-size: 21px; letter-spacing: -2px; }
  .corner.top { top: 6px; left: 8px; }
  .corner.bottom { bottom: 6px; right: 8px; }

  .tone-red .value { color: var(--red); }
  .tone-red .corner { color: var(--red-dark); }
  .tone-green .value { color: var(--green); }
  .tone-green .corner { color: var(--green-dark); }
  .tone-purple .value { color: var(--purple); }
  .tone-purple .corner { color: var(--purple-dark); }
  .tone-blue .value { color: var(--blue); }
  .tone-blue .corner { color: var(--blue-dark); }

  .action-card .art {
    position: absolute;
    left: 18px; right: 18px;
    top: 8px; height: 150px;
    border-radius: 12px;
    display: flex;
    align-items: center;
    justify-content: center;
  }
  .action-card .art-name {
    font-family: "Fira Sans Extra Condensed", sans-serif;
    font-weight: 600;
    font-size: 54px;
    line-height: 1;
    color: #ffffff;
  }
  .action-card .label {
    position: absolute;
    left: 0; right: 0;
    bottom: 8px;
    text-align: center;
    font-family: "Fira Sans Extra Condensed", sans-serif;
    font-weight: 600;
    font-size: 27px;
    line-height: 1;
  }
  .burn .art { background: linear-gradient(160deg, var(--red) 0%, var(--red-dark) 100%); }
  .burn .label { color: var(--red); }
  .add .art { background: linear-gradient(160deg, var(--green) 0%, var(--green-dark) 100%); }
  .add .label { color: var(--green); }
  .reset .art { background: linear-gradient(160deg, var(--purple) 0%, var(--purple-dark) 100%); }
  .reset .label { color: var(--purple); }
  .take .art { background: linear-gradient(160deg, #8a8a8a 0%, #111111 100%); }
  .take .label { color: var(--ink); }

  .card-back .frame {
    position: absolute;
    inset: 3px;
    border: 2px solid var(--blue-dark);
  }
  .card-back .game-name {
    position: absolute;
    left: 0; right: 0;
    top: 50%;
    transform: translateY(-50%);
    text-align: center;
    font-family: "Fira Sans Extra Condensed", sans-serif;
    font-weight: 600;
    font-size: 96px;
    line-height: 1;
    color: var(--blue);
  }
</style>
</head>
<body>
<main class="deck">
  <div class="card number-card tone-red col-1 row-1"><span class="corner top">1</span><span class="value">1</span><span class="corner bottom">1</span></div>
  <div class="card number-card tone-green col-2 row-1"><span class="corner top">2</span><span class="value">2</span><span class="corner bottom">2</span></div>
  <div class="card number-card tone-purple col-3 row-1"><span class="corner top">3</span><span class="value">3</span><span class="corner bottom">3</span></div>
  <div class="card number-card tone-blue col-4 row-1"><span class="corner top">4</span><span class="value">4</span><span class="corner bottom">4</span></div>

  <div class="card number-card tone-red col-1 row-2"><span class="corner top">5</span><span class="value">5</span><span class="corner bottom">5</span></div>
  <div class="card number-card tone-green col-2 row-2"><span class="corner top">6</span><span class="value">6</span><span class="corner bottom">6</span></div>
  <div class="card number-card tone-purple col-3 row-2"><span class="corner top">7</span><span class="value">7</span><span class="corner bottom">7</span></div>
  <div class="card number-card tone-blue col-4 row-2"><span class="corner top">8</span><span class="value">8</span><span class="corner bottom">8</span></div>

  <div class="card number-card tone-red col-1 row-3"><span class="corner top">9</span><span class="value">9</span><span class="corner bottom">9</span></div>
  <div class="card number-card tone-green col-2 row-3"><span class="corner top">10</span><span class="value two-digit">10</span><span class="corner bottom">10</span></div>

  <div class="card action-card burn col-3 row-3">
    <div class="art" role="img" aria-label="Flame artwork around the game name"><span class="art-name">zo</span></div>
    <span class="label">BURN zo</span>
  </div>
  <div class="card action-card add col-4 row-3">
    <div class="art" role="img" aria-label="Plus sign artwork with the game name"><span class="art-name">zo</span></div>
    <span class="label">Add zo</span>
  </div>

  <div class="card action-card reset col-1 row-4">
    <div class="art" role="img" aria-label="Circular reset arrow artwork around the game name"><span class="art-name">zo</span></div>
    <span class="label">Reset zo</span>
  </div>
  <div class="card action-card take col-2 row-4">
    <div class="art" role="img" aria-label="Dark artwork of the game name gathering many smaller copies"><span class="art-name">zo</span></div>
    <span class="label">Take zo</span>
  </div>

  <div class="card card-back col-4 row-4">
    <div class="frame"></div>
    <span class="game-name">zo</span>
  </div>
</main>
</body>
</html>
```